Geschäftspapiere für Bauunternehmen
Zielgruppe
Wir sind ein Bauunternehmen.
Aufgabenstellung
Bitte das Briefpapier alles nötige für eine Angebotserstellung sowie Rechnungsstellung hinzufügen. Heißt: Logo, Firma, Firmensitz, Telefonnummer, Steuernummer und Bankdaten. Bankdaten: DE41 5807 1143 2296 0183 77 BIC: TRWKDEFFXXX

```html
<!DOCTYPE html>
<html lang="de">
<head>
<meta charset="utf-8">
<title>Brandt Bau – Briefpapier</title>
<link href="https://fonts.googleapis.com/css2?family=Montserrat:wght@400;500;600&display=swap" rel="stylesheet">
<style>
  :root {
    --bg: #efefef;
    --paper: #f2f2f2;
    --ink: #1b1b1b;
    --brand-red: #c8050d;
    --sign-tone: #e4e4e4;
  }
  * { margin: 0; padding: 0; box-sizing: border-box; }
  html, body {
    width: 949px; height: 1200px; overflow: hidden;
    background: var(--bg);
    font-family: "Montserrat", sans-serif;
    color: var(--ink);
  }
  .letterhead {
    position: absolute; left: 50px; top: 0;
    width: 850px; height: 1200px;
    background: var(--paper);
  }
  .letterhead > * { position: absolute; white-space: nowrap; }

  .brand { left: 46px; top: 186px; display: flex; align-items: center; gap: 14px; }
  .brand-name { font-size: 37px; font-weight: 400; letter-spacing: 0.5px; line-height: 1; }
  .brand-mark { width: 22px; height: 22px; background: var(--brand-red); }
  .head-rule { left: 46px; top: 234px; width: 736px; height: 2px; background: var(--ink); }

  .sender { left: 46px; top: 320px; font-size: 15px; line-height: 1.1; }
  .sender .address { margin-bottom: 9px; }
  .sender .phone,
  .sender .email,
  .sender .tax-id { margin-bottom: 8px; font-size: 16px; }

  .company { left: 580px; top: 314px; }
  .company-name { font-size: 27px; font-weight: 600; line-height: 1; }
  .company-type { font-size: 16px; margin-top: 4px; }

  .body-text { left: 46px; top: 526px; font-size: 16px; line-height: 25px; }
  .body-text p { margin-bottom: 26px; }
  .body-text p.closing { margin-bottom: 0; }

  .outro { left: 50px; top: 857px; font-size: 16px; line-height: 41px; }

  .signature { left: 53px; top: 998px; width: 212px; height: 38px; background: var(--sign-tone); }
  .sign-role { left: 50px; top: 1048px; font-size: 16px; }

  .hours { left: 48px; top: 1104px; font-size: 16px; line-height: 27px; }
  .bank { left: 533px; top: 1104px; font-size: 16px; line-height: 27px; }
</style>
</head>
<body>
  <main class="letterhead">
    <div class="brand">
      <span class="brand-name">BRANDT BAU</span>
      <span class="brand-mark"></span>
    </div>
    <div class="head-rule"></div>

    <div class="sender">
      <div class="address">Lindenstraße 42,<br>10969 Berlin, Germany</div>
      <div class="phone">030 512 44 806</div>
      <div class="email">info@brandt-bau.de</div>
      <div class="tax-id">Steuernummer: 29/451/03817</div>
    </div>

    <div class="company">
      <div class="company-name">Brandt Bau</div>
      <div class="company-type">Bauunternehmen</div>
    </div>

    <div class="body-text">
      <p>Guten Tag,</p>
      <p>anliegend übersende ich Ihnen die Bestätigung Ihrer Gewerbeanmeldung.</p>
      <p class="closing">Mit freundlichen Grüßen<br>im Auftrag<br>Kessler</p>
    </div>

    <div class="outro">
      Wir sind gern für Sie da. Wir schätzen unsere Kunden sehr.<br>
      Mit freundlichen Grüßen
    </div>

    <div class="signature" role="img" aria-label="Handschriftliche Unterschrift Brandt Bau"></div>
    <div class="sign-role">Bauunternehmen</div>

    <div class="hours">Montag bis Freitag von 08.00-17.00 Uhr</div>
    <div class="bank">DE41 5807 1143 2296 0183 77<br>BIC: TRWKDEFFXXX</div>
  </main>
</body>
</html>
```